we are an outdoor outlet in a country club that has a variety of outlets. The Club is called Lanterns and is located in Cairo, Egypt. This garden menu will include cuisines from the Mediterranean, Asia and Texmex. we need a menu that is colorful and would fit an A3 size, back and front are to be used. Attached is the old menu currently in use (Garden Menu 2012.pdf is just for reference) and the new menu text for you to use is under the name Garden Menu Fall 2013
thank you.

```html
<!DOCTYPE html>
<html lang="en">
<head>
<meta charset="utf-8">
<title>Lanterns Country Club – Garden Menu</title>
<link rel="stylesheet" href="https://fonts.googleapis.com/css2?family=Dancing+Script:wght@500;700&family=Didact+Gothic&family=Quicksand:wght@400;500&display=swap">
<style>
:root{
  --sand:#e4dfd6;
  --paper:#ffffff;
  --magenta:#b02a5b;
  --wine:#5b2b33;
  --olive:#8f9a2e;
  --lime:#b5c33c;
  --teal:#2f7fa6;
  --ink:#6a5a5c;
  --rule:#c9a0ad;
}
*{margin:0;padding:0;box-sizing:border-box}
html,body{width:1200px;height:1200px;overflow:hidden;background:#eef0ee}
.menu{position:relative;width:1200px;height:1200px;display:flex;background:var(--paper);font-family:"Quicksand",sans-serif;color:var(--ink)}
.sidebar{width:310px;background:var(--sand);position:relative;padding:60px 30px;border-right:2px dashed var(--rule)}
.menu-title{font-family:"Dancing Script",cursive;font-weight:700;color:var(--magenta);font-size:62px;line-height:1}
.club-name{margin:70px auto 0;width:190px;height:190px;border-radius:50%;background:#f3efe9;display:flex;flex-direction:column;align-items:center;justify-content:center;font-family:"Didact Gothic",sans-serif;color:var(--wine);font-size:34px}
.floral{position:absolute;left:0;bottom:0;width:310px;height:620px;background:linear-gradient(160deg,rgba(181,195,60,.35),rgba(176,42,91,.45) 60%,rgba(91,43,51,.5))}
.content{flex:1;display:flex;padding:50px 36px 30px 40px;gap:30px}
.column{flex:1}
.divider{width:14px;background:linear-gradient(var(--rule),#e8c8d2,var(--rule));opacity:.6;border-radius:7px}
.corner-title{font-family:"Dancing Script",cursive;font-weight:700;color:var(--wine);font-size:44px;text-align:center;border-bottom:2px solid var(--lime);padding-bottom:6px;margin-bottom:18px}
h2{font-family:"Didact Gothic",sans-serif;font-weight:400;font-size:26px;text-align:center;margin:18px 0 10px}
h2.pink{color:var(--magenta)} h2.wine{color:var(--wine)} h2.olive{color:var(--olive)} h2.teal{color:var(--teal)}
.dish{margin-bottom:10px}
.dish-name{font-family:"Dancing Script",cursive;font-weight:700;font-size:25px;color:var(--wine);line-height:1.1}
.dish-desc{font-size:12.5px;display:flex;justify-content:space-between;gap:8px}
.price{white-space:nowrap;color:var(--wine)}
.list{list-style:none}
.list li{font-size:13px;display:flex;gap:6px;margin-bottom:5px}
.list li::before{content:"✱";color:var(--magenta)}
.list .fill{flex:1;border-bottom:1px dotted var(--ink);transform:translateY(-4px)}
.note{font-size:13px;color:var(--magenta);text-align:center;margin-bottom:8px}
.sub{font-size:13px;margin:4px 0 10px}
.sub b{color:var(--magenta);font-weight:500}
</style>
</head>
<body>
<main class="menu">
  <aside class="sidebar">
    <h1 class="menu-title">Garden Menu</h1>
    <div class="club-name">Lanterns</div>
    <div class="floral" role="img" aria-label="Illustrated bouquet of pink and maroon flowers with green leaves"></div>
  </aside>
  <section class="content">
    <div class="column">
      <div class="corner-title">Mediterranean Corner</div>
      <h2 class="pink">Soups</h2>
      <div class="dish"><div class="dish-name">Tomato Basil</div><div class="dish-desc"><span>Simmered tomato soup finished with fresh basil and cream.</span><span class="price">EL 00.00</span></div></div>
      <div class="dish"><div class="dish-name">Chicken Cream</div><div class="dish-desc"><span>Chicken broth with roasted chicken cubes, pine nuts and cream.</span><span class="price">EL 00.00</span></div></div>
      <div class="dish"><div class="dish-name">Moroccan Harira</div><div class="dish-desc"><span>Vegetable broth with fresh tomato, chickpeas, lentils, cilantro and sliced lamb.</span><span class="price">EL 00.00</span></div></div>
      <h2 class="wine">Appetizers</h2>
      <ul class="list">
        <li>Salmon tartare seasoned with lemon juice, garlic and black pepper<span class="fill"></span><span class="price">EL 00.00</span></li>
        <li>Roasted eggplant rolls with herbed ricotta and pine nuts<span class="fill"></span><span class="price">EL 00.00</span></li>
        <li>Foteer mini pita served with tahina and oriental salsa<span class="fill"></span><span class="price">EL 00.00</span></li>
        <li>Moutabal with thyme and olive oil<span class="fill"></span><span class="price">EL 00.00</span></li>
        <li>Fried kobeba with minced meat, spices and pine nuts<span class="fill"></span><span class="price">EL 00.00</span></li>
        <li>Fried cauliflower with tahina served with pita<span class="fill"></span><span class="price">EL 00.00</span></li>
        <li>Sambousek with herbed white cheese and mint<span class="fill"></span><span class="price">EL 00.00</span></li>
        <li>Oriental sausage sauteed with garlic and onion<span class="fill"></span><span class="price">EL 00.00</span></li>
        <li>Mini vine leaves with a yoghurt dip<span class="fill"></span><span class="price">EL 00.00</span></li>
        <li>Fatoush with a pomegranate syrup dressing<span class="fill"></span><span class="price">EL 00.00</span></li>
        <li>Hummus seasoned with lemon juice, garlic and olive oil<span class="fill"></span><span class="price">EL 00.00</span></li>
        <li>White cheese with diced tomato, thyme and olive oil<span class="fill"></span><span class="price">EL 00.00</span></li>
        <li>Tehina seasoned with cumin, lemon juice and garlic<span class="fill"></span><span class="price">EL 00.00</span></li>
      </ul>
      <h2 class="olive">Salads</h2>
      <div class="dish"><div class="dish-name">Caprese</div><div class="dish-desc"><span>Buffalo mozzarella and sliced tomato with a balsamic vinaigrette.</span><span class="price">EL 00.00</span></div></div>
      <div class="dish"><div class="dish-name">Rocket Apple</div><div class="dish-desc"><span>Rocket leaves with gorgonzola, croutons and strawberry vinaigrette.</span><span class="price">EL 00.00</span></div></div>
      <div class="dish"><div class="dish-name">French Riviera Niçoise</div><div class="dish-desc"><span>Lettuce, egg, tomato, tuna, olives, onion and celery.</span><span class="price">EL 00.00</span></div></div>
    </div>
    <div class="divider" role="img" aria-label="Vertical ornamental chain border"></div>
    <div class="column">
      <h2 class="teal">Pizza &amp; Pasta</h2>
      <div class="dish"><div class="dish-name">Lasagna</div></div>
      <div class="dish"><div class="dish-name">Pizza Margarita</div></div>
      <div class="dish"><div class="dish-name">Create your own pasta</div></div>
      <p class="sub"><b>Sauces</b> Napolitana, Bolognese, Alfredo</p>
      <h2 class="pink">Toppings</h2>
      <ul class="list">
        <li>Bell peppers, olives, tomato</li>
        <li>Mushroom, chicken, tuna</li>
        <li>Smoked salmon, shrimps</li>
      </ul>
      <h2 class="teal">Sandwiches</h2>
      <p class="note">Served with French fries or a green salad</p>
      <ul class="list">
        <li>Beef or chicken Shawerma<span class="fill"></span><span class="price">EL 00.00</span></li>
        <li>Grilled kofta<span class="fill"></span><span class="price">EL 00.00</span></li>
        <li>Greek lamb gyro in pita bread with Tzatziki<span class="fill"></span><span class="price">EL 00.00</span></li>
        <li>Club sandwich with smoked beef, turkey, egg<span class="fill"></span><span class="price">EL 00.00</span></li>
      </ul>
      <h2 class="pink">Main Courses</h2>
      <div class="dish"><div class="dish-name">Veal Parmeggiana</div><div class="dish-desc"><span>Breaded veal escalope topped with melted cheese and tomato sauce.</span><span class="price">EL 00.00</span></div></div>
      <div class="dish"><div class="dish-name">Chicken a la Francaise</div><div class="dish-desc"><span>Pan fried chicken breast in a mushroom cream sauce with vegetables.</span><span class="price">EL 00.00</span></div></div>
      <div class="dish"><div class="dish-name">Grilled Salmon</div><div class="dish-desc"><span>Salmon steak charcoal grilled with avocado and tomato relish.</span><span class="price">EL 00.00</span></div></div>
      <div class="dish"><div class="dish-name">Moroccan Chicken</div><div class="dish-desc"><span>Slow cooked chicken with preserved lemon, olives and couscous.</span><span class="price">EL 00.00</span></div></div>
    </div>
  </section>
</main>
</body>
</html>
```